Puristisch-modernes Webdesign für eine Anwaltskanzlei
Zielgruppe
Wir sind eine Patent- und Rechtsanwaltskanzlei mit Sitz in Frankfurt am Main, die inzwischen seit 15 Jahren besteht und den Fokus auf den 'Gewerblichen Rechtsschutz' und das Geistige Eigentum hat.
Unsere Kanzlei berät Mandanten ausführlich zu den Themen 'Patentrecht, Schutzstrategien, Patentanmeldung, Recherche, Geheimhaltungsvereinbarungen, Patentverletzung, Arbeitnehmererfindung und Streitverfahren'.
Unsere Kernzielgruppe kommt aus Deutschland bzw. der DACH-Region, ist männlich, zwischen 18 - 49 Jahren alt und technikaffin. Wir haben allerdings auch Mandanten aus China, der Türkei und den USA. Wir sprechen vorrangig mittlere und größere Unternehmen an.
Aufgabenstellung
Wir legen sehr viel wert auf eine hochwertige und puristische neue Homepage, die im Web 2.0 (oder gibt es heutzutage schon 3.0? ;-) ) angekommen ist. Sachen wie mobile-friendly sind für uns eine Selbstverständlichkeit. Das Thema "One-Pager" ist sicherlich klasse, aufgrund unseres Erklärungsbedarfs und bspw. den Anwalts-Vorstellungen scheidet dieser jedoch aus.
Wichtig: Wir würden gerne unsere aktuelle Link-Struktur beibehalten, damit wir aus SEO-Sicht keine Einbüße haben.
Um Ihnen Eindrücke zu geben, welche (unserer Meinung nach) positiven Beispiele es gibt, möchte ich Ihnen zwei Links mitgeben:
• http://deutschland.brennholtvarga.com (vor allem die Navigation und das Dropdown-Menü sehen sehr gut aus; auch das clean-e und puristische Design sind gut, Wording für EN/DE-Seite sehr gut - also dass es ausgeschrieben ist, bspw. "Deutsch" / "English" / "Chinese" / "Turkish"; Footer sehr schön strukturiert)
• http://www.weiler-lawfirm.com/home.html (Slider ist klasse, Social Media Buttons rechts oben gut eingebunden aber leider nicht im Chatterbook-Blau, Flitter-Blau, Zoogle-Rot etc. :-( , rechte Seite Veranstaltungen + Publikationen etc. gut)
• http://www.bromsel.de/ (Hier finden wir unten die Aufteilung in drei Blöcke sehr schön. Ggf. bei uns dann: "Die letzten Artikel" / "Über die Kanzlei" / "Unser Team")
Was noch unbedingt zu berücksichtigen ist: Wir haben einen sehr gut geführten und aktiven Blog (INFO.juris-vantor.com). Darein fließen auch viele Ressourcen.
Es ist sehr wohl denkbar, dass wir bereits auf der Kanzlei-Seite (WWW.juris-vantor.com) bspw. die letzten 3 deutschsprachigen und 3 englischsprachigen Artikel aufführen, um den User (auch) auf unseren Blog führen und quasi interne Verlinkungen machen.
Abschließend: Das Design soll auf das CMS "Wordpress" optimiert werden.

```html
<!DOCTYPE html>
<html lang="de">
<head>
<meta charset="utf-8">
<title>KLVORAX – Patent- & Rechtsanwaltskanzlei</title>
<link href="https://fonts.googleapis.com/css2?family=Open+Sans:wght@300;400;600;700&display=swap" rel="stylesheet">
<style>
:root{
  --orange:#e64a07;
  --dark:#5a4f4c;
  --text:#5b5553;
  --muted:#7b7573;
  --sand:#f2f0ec;
  --line:#cfcac6;
  --white:#fff;
}
*{box-sizing:border-box;margin:0;padding:0}
html,body{width:692px;height:1200px;overflow:hidden}
body{position:relative;font-family:'Open Sans',sans-serif;color:var(--text);background:var(--white)}
.abs{position:absolute}
.btn{position:absolute;background:var(--dark);color:var(--white);font-size:4.8px;font-weight:600;display:flex;align-items:center;justify-content:center;letter-spacing:.1px}
.rule{width:22px;height:1.5px;background:var(--orange);margin:0 auto}
/* header */
.brand{left:134px;top:6px;display:flex;align-items:center;gap:4px}
.brand-mark{width:14px;height:14px;background:var(--orange)}
.brand-name{font-size:11px;font-weight:600;color:var(--orange);letter-spacing:.5px}
.brand-tag{left:134px;top:22px;font-size:4.6px;color:var(--muted);letter-spacing:.3px}
.lang{left:349px;top:16px;font-size:6.6px;color:var(--muted)}
.social{left:398px;top:15px;display:flex;gap:2.5px}
.social span{width:11px;height:11px;border-radius:50%;display:block}
.phone{left:480px;top:16px;font-size:6.4px;font-weight:600;color:var(--text);display:flex;gap:2px;align-items:center}
.nav{left:134px;top:32px;width:424px;height:18px;border-top:.6px solid var(--line);border-bottom:.6px solid var(--line);display:flex;justify-content:space-between;align-items:center;font-size:6.6px;font-weight:600;color:var(--text)}
.nav .active{position:relative}
.nav .active:after{content:"";position:absolute;left:-10px;right:-10px;bottom:-5.5px;height:1.5px;background:var(--dark)}
.nav .blog{color:var(--orange)}
/* hero */
.hero-band{left:0;top:54px;width:692px;height:141px;background:var(--sand)}
.hero-gap{left:127px;top:54px;width:438px;height:141px;background:var(--white)}
.hero-img{left:134px;top:54px;width:289px;height:141px;background:linear-gradient(160deg,#ddd6cc,#c9beb1 60%,#b9ad9f)}
.hero-panel{left:423px;top:54px;width:135px;height:141px;background:var(--orange);color:var(--white);text-align:center}
.hero-panel h1{font-weight:400;font-size:11px;line-height:14.5px;margin-top:6px}
.hero-panel p{font-size:6.6px;line-height:11px;margin-top:5px}
.dots{display:flex;gap:2.5px;justify-content:center}
.dots i{width:5px;height:5px;border-radius:50%;background:var(--white);display:block}
/* intro */
.intro{left:134px;top:206px;width:279px;text-align:center}
.intro h2{font-weight:400;font-size:11.2px;line-height:14.5px;color:var(--text)}
.intro p{font-size:6.7px;line-height:10.9px;color:var(--muted);margin-top:6px}
.acc{position:absolute;left:134px;width:279px;border:.7px solid var(--orange);font-size:6.7px;font-weight:500;padding:0 7px;display:flex;align-items:center;justify-content:space-between;color:var(--text)}
.acc.open{background:var(--orange);color:var(--white);display:block;padding:6px 7px}
.acc.open .head{display:flex;justify-content:space-between;font-weight:600}
.acc.open p{font-size:6.7px;line-height:10.9px;margin-top:9px}
.chev{width:9px;height:9px;display:block}
/* sidebar */
.side{left:423px;width:135px;background:var(--sand);text-align:center;padding-top:6px}
.side h3{font-weight:400;font-size:11px;color:var(--text);margin-bottom:9px}
.event{font-size:4.9px;line-height:6.4px;margin-bottom:6px;padding:0 8px}
.event b{font-weight:700}
.event .date{font-weight:700;display:block;margin-top:2px}
.event .date:before,.pubs li:before{content:"";display:inline-block;width:3px;height:3px;background:var(--orange);margin-right:3px;vertical-align:middle}
.event.hl{color:var(--orange)}
.pubs{list-style:none;text-align:left;padding-left:15px;font-size:5.1px;font-weight:600}
.pubs li{margin-bottom:7.5px}
.pubs li:before{margin-right:5px}
/* three blocks */
.band{left:0;top:507px;width:692px;height:184px;background:var(--sand)}
.col-title{position:absolute;top:513px;font-size:7.4px;font-weight:600;color:var(--orange)}
.card{position:absolute;top:525px;width:134px;height:152px;background:var(--white)}
.card .img{height:64px;position:relative}
.arrow{position:absolute;top:52px;width:8.5px;height:8.5px;border-radius:50%;background:var(--orange);display:flex;align-items:center;justify-content:center}
.card .body{padding:5px 7px}
.date{font-size:5px;color:var(--muted)}
.ttl{font-size:7px;line-height:8.6px;font-weight:700;color:var(--dark);margin-top:4px;padding-bottom:4px;border-bottom:.6px solid var(--orange)}
.txt{font-size:4.9px;line-height:6.5px;color:var(--muted);margin-top:5px}
.bul{list-style:none;font-size:5px;line-height:6.5px;color:var(--muted);margin-top:5px}
.bul li{padding-left:8px;position:relative;margin-bottom:2.2px}
.bul li:before{content:"";position:absolute;left:0;top:2px;width:3px;height:3px;background:var(--orange)}
/* blog sections */
.sec-head{position:absolute;left:0;width:692px;text-align:center;font-weight:400;font-size:11px;color:var(--text)}
.sec-head .rule{margin-top:5px}
.post{position:absolute;width:134px;padding:6px 7px}
.post.hot{background:var(--orange)}
.post.hot .date,.post.hot .ttl,.post.hot .txt{color:var(--white);border-color:var(--white)}
/* awards */
.awards{left:134px;top:1017px;width:424px;height:106px;border:.6px solid var(--line);display:flex}
.awards > div{flex:1;border-right:.6px solid var(--line);display:flex;align-items:center;justify-content:center;position:relative}
.awards .cta{background:var(--orange);border:none;flex-direction:column;color:var(--white);font-size:5px;line-height:8.6px;text-align:center;padding:0 12px}
.pdots{left:339px;top:1129px;display:flex;gap:2px}
.pdots i{width:5px;height:5px;border-radius:50%;border:.6px solid var(--orange);display:block}
/* footer */
.footer{left:0;top:1148px;width:692px;height:52px;background:var(--dark);color:var(--white);font-size:5.2px;font-weight:600}
.fcol{position:absolute;top:8px;line-height:10.9px}
.ficon{position:absolute;width:6.5px;height:6.5px;background:var(--orange);border-radius:1px}
.fl li{list-style:none;padding-left:8px;position:relative}
.fl li:before{content:"";position:absolute;left:0;top:4px;width:3px;height:3px;background:var(--orange)}
</style>
</head>
<body>

<!-- Header -->
<div class="abs brand"><span class="brand-mark"></span><span class="brand-name">KLVORAX</span></div>
<div class="abs brand-tag">PATENT- &amp; RECHTSANWALTSKANZLEI · DR. KESSLER-BRANDT &amp; PARTNERS LLP</div>
<div class="abs lang">Deutsch ⌄</div>
<div class="abs social">
  <span style="background:#0077b5" aria-label="Linkora"></span>
  <span style="background:#1da1f2" aria-label="Flitter"></span>
  <span style="background:#3b5998" aria-label="Chatterbook"></span>
  <span style="background:#026466" aria-label="Zunga"></span>
  <span style="background:#dd4b39" aria-label="Zoogle"></span>
</div>
<div class="abs phone">
  <svg width="6" height="6" viewBox="0 0 10 10"><path d="M2 0.5 L4 3 L3 4 Q4.5 6.2 6 7 L7 6 L9.5 8 L8.5 9.5 Q3 9 0.5 1.5 Z" fill="#5b5553"/></svg>
  +49 (0) 69 / 555 014 - 0
</div>
<nav class="abs nav">
  <span>LEISTUNGEN ⌄</span><span>KANZLEI ⌄</span><span class="active">KONTAKT ⌄</span><span>KARRIERE</span><span>NEUIGKEITEN ⌄</span><span class="blog">■ BLOG</span>
</nav>

<!-- Hero -->
<div class="abs hero-band"></div>
<div class="abs hero-gap"></div>
<div class="abs hero-img" role="img" aria-label="Foto: zwei Kinder in Kostümen mit Kabel und Maschinenteilen auf hellem Boden"></div>
<div class="abs hero-panel">
  <h1>LOREM IPSUM<br>DOLOR SIT AMET,<br>CONSECTETUER<br>ADIPISCING ELIT.</h1>
  <p>Nullam dictum felis eu pede mollis<br>pretium. Integer tincidunt.</p>
  <div class="btn" style="left:37px;top:98px;width:62px;height:14px">MEHR ERFAHREN</div>
  <div class="dots abs" style="left:0;right:0;top:130px"><i style="background:var(--dark)"></i><i></i><i></i><i></i></div>
</div>

<!-- Intro -->
<div class="abs intro">
  <h2>CUM SOCIIS NATOQUE PENATIBUS ET MAGNIS DIS PARTURIENT MONTES, NASCETUR RIDICULUS MUS.</h2>
  <div class="rule" style="margin-top:5px"></div>
  <p>Donec quam felis, ultricies nec, pellentesque eu, pretium quis, sem. Nulla consequat massa quis enim. Donec pede justo, fringilla vel, aliquet nec, vulputate eget, arcu. In enim justo, rhoncus ut, imperdiet a, venenatis vitae, justo. Nullam dictum felis eu pede mollis pretium. Integer tincidunt. Cras dapibus. Vivamus elementum semper nisi. Aenean vulputate eleifend tellus. Aenean leo ligula, porttitor eu, consequat vitae, eleifend ac, enim.</p>
</div>

<div class="acc" style="top:312px;height:18px">Wir beraten Sie zu Patenten, Marken &amp; Designs
  <svg class="chev" viewBox="0 0 10 10"><rect x=".5" y=".5" width="9" height="9" fill="none" stroke="#e64a07"/><path d="M3 4 L5 6 L7 4" fill="none" stroke="#e64a07"/></svg></div>
<div class="acc" style="top:333px;height:18px">Patentanmeldung / Eintragung von Marken &amp; Designs
  <svg class="chev" viewBox="0 0 10 10"><rect x=".5" y=".5" width="9" height="9" fill="none" stroke="#e64a07"/><path d="M3 4 L5 6 L7 4" fill="none" stroke="#e64a07"/></svg></div>
<div class="acc open" style="top:355px;height:94px">
  <div class="head">Hilfe bei Patent-, Marken-, Design- &amp; Urheberrechtsverletzung
    <svg class="chev" viewBox="0 0 10 10"><rect x=".5" y=".5" width="9" height="9" fill="none" stroke="#fff"/><path d="M3 6 L5 4 L7 6" fill="none" stroke="#fff"/></svg></div>
  <p>Jede Verletzung Ihres geistigen Eigentums kann Umsätze und Image Ihres Unternehmens nachhaltig beschädigen. Wir suchen gemeinsam mit Ihnen nach der besten Lösung und helfen, Patente, Marken, Designs und Urheberrechte zu verteidigen und durchzusetzen.</p>
  <div class="btn" style="left:7px;top:72px;width:62px;height:14px">MEHR ERFAHREN</div>
</div>
<div class="acc" style="top:453px;height:18px">Verteidigung gegen Abmahnungen &amp; Grenzbeschlagnahme
  <svg class="chev" viewBox="0 0 10 10"><rect x=".5" y=".5" width="9" height="9" fill="none" stroke="#e64a07"/><path d="M3 4 L5 6 L7 4" fill="none" stroke="#e64a07"/></svg></div>
<div class="acc" style="top:475px;height:18px">Wir sind ISO-zertifiziert!
  <svg class="chev" viewBox="0 0 10 10"><rect x=".5" y=".5" width="9" height="9" fill="none" stroke="#e64a07"/><path d="M3 4 L5 6 L7 4" fill="none" stroke="#e64a07"/></svg></div>

<!-- Sidebar -->
<aside class="abs side" style="top:210px;height:112px">
  <h3>VERANSTALTUNGEN</h3>
  <div class="rule" style="margin:-6px auto 7px"></div>
  <div class="event"><b>Aliquam lorem ante, dapibus in, viverra quis.</b><br>Feugiat a, tellus. Phasellus viverra nulla ut me...<span class="date">16. Juni 2016 - München</span></div>
  <div class="event"><b>Aliquam lorem ante, dapibus in, viverra quis.</b><br>Feugiat a, tellus. Phasellus viverra nulla ut me...<span class="date">16. Juni 2016 - München</span></div>
  <div class="event hl"><b>Aliquam lorem ante, dapibus in, viverra quis.</b><br>Feugiat a, tellus. Phasellus viverra nulla ut me...<span class="date">16. Juni 2016 - München</span></div>
</aside>
<aside class="abs side" style="top:326px;height:102px">
  <h3>PUBLICATIONEN</h3>
  <div class="rule" style="margin:-6px auto 11px"></div>
  <ul class="pubs"><li>Aliquam lorem ante,</li><li>In enim justo, rhoncus ut.</li><li>Nullam dictum felis eu pede.</li><li>Aenean massa.</li><li>Aliquam lorem ante.</li></ul>
</aside>

<!-- Three blocks -->
<div class="abs band"></div>
<div class="col-title" style="left:134px">DIE LETZTEN ARTIKEL</div>
<div class="col-title" style="left:279px">ÜBER DIE KANZLEI</div>
<div class="col-title" style="left:423px">UNSER TEAM</div>

<article class="card" style="left:134px">
  <div class="img" role="img" aria-label="Foto: Auslage mit vielen bunten Ledergürteln" style="background:linear-gradient(135deg,#7a5a46,#b6a597 50%,#5d6b7c)">
    <span class="arrow" style="left:7px"><svg width="4" height="4" viewBox="0 0 10 10"><path d="M6.5 2 L3.5 5 L6.5 8" fill="none" stroke="#fff" stroke-width="2"/></svg></span>
    <span class="arrow" style="right:7px"><svg width="4" height="4" viewBox="0 0 10 10"><path d="M3.5 2 L6.5 5 L3.5 8" fill="none" stroke="#fff" stroke-width="2"/></svg></span>
  </div>
  <div class="body">
    <div class="date">6. Juni 2016</div>
    <div class="ttl">PRODUKTPIRATERIE: ZAHL DER FÄLSCHUNGEN WÄCHST WEITER</div>
    <p class="txt">Der internationale Handel mit illegalen Imitaten und Produktfälschungen verursacht laut einer neuen Studie der Europäische Beobachtungsstelle und der Organisation für wirtschaftliche Zusammenarbeit und Entwicklung (OWZE) einen finanziellen Schaden von bis zu 340 Milliarden Euro pro...</p>
  </div>
</article>
<article class="card" style="left:279px">
  <div class="img" role="img" aria-label="Foto: Aktenregister mit Reiter „Patents“" style="background:linear-gradient(180deg,#e9e3d6,#c9c2b5 60%,#d9b8bb)">
    <span class="arrow" style="left:7px"><svg width="4" height="4" viewBox="0 0 10 10"><path d="M6.5 2 L3.5 5 L6.5 8" fill="none" stroke="#fff" stroke-width="2"/></svg></span>
    <span class="arrow" style="right:7px"><svg width="4" height="4" viewBox="0 0 10 10"><path d="M3.5 2 L6.5 5 L3.5 8" fill="none" stroke="#fff" stroke-width="2"/></svg></span>
  </div>
  <div class="body">
    <div class="date">14. April 2016</div>
    <div class="ttl">TAREK ÜNAL WIRD PARTNER VON DR. KESSLER-BRANDT &amp; PARTNERS LLP</div>
    <p class="txt">Der zuvor als Associate tätige Rechtsanwalt Tarek Ünal ist seit Mitte April 2016 neuer Partner der Patent- und Rechtsanwaltskanzlei Dr. Kessler-Brandt &amp; Partners LLP. Bereits seit 2013 arbeitet Tarek bei uns als Rechtsanwalt, seit dieser ...</p>
  </div>
</article>
<article class="card" style="left:423px">
  <div class="img" role="img" aria-label="Porträtfoto eines Partners" style="background:linear-gradient(180deg,#f4f2f0,#ddd8d4)">
    <span class="arrow" style="left:7px"><svg width="4" height="4" viewBox="0 0 10 10"><path d="M6.5 2 L3.5 5 L6.5 8" fill="none" stroke="#fff" stroke-width="2"/></svg></span>
    <span class="arrow" style="right:7px"><svg width="4" height="4" viewBox="0 0 10 10"><path d="M3.5 2 L6.5 5 L3.5 8" fill="none" stroke="#fff" stroke-width="2"/></svg></span>
  </div>
  <div class="body">
    <div class="date">&nbsp;</div>
    <div class="ttl">DR. FRIEDRICH-ANTON KESSLER-BRANDT</div>
    <ul class="bul"><li>Dipl. Chem. und Apotheker</li><li>Patentanwalt</li><li>European Patent Attorney</li><li>Europäischer Marken- und Geschmacksmusteranwalt</li></ul>
  </div>
</article>

<!-- German blog -->
<h2 class="sec-head" style="top:698px">DIE LETZTEN ARTIKEL AUS UNSEREM DEUTSCHEN BLOG<div class="rule"></div></h2>
<article class="post" style="left:134px;top:724px">
  <div class="date">6. Juni 2016</div>
  <div class="ttl" style="border:none">PRODUKTPIRATERIE: ZAHL DER FÄLSCHUNGEN WÄCHST WEITER</div>
  <p class="txt">Der internationale Handel mit illegalen Imitaten und Produktfälschungen verursacht laut einer neuen Studie der Europäische Beobachtungsstelle und der Organisation für wirtschaftliche Zusammenarbeit und Entwicklung (OWZE) einen finanziellen Schaden von bis zu 340 Milliarden Euro pro...</p>
</article>
<article class="post hot" style="left:279px;top:724px;height:87px">
  <div class="date">6. Juni 2016</div>
  <div class="ttl" style="border:none">PRODUKTPIRATERIE: ZAHL DER FÄLSCHUNGEN WÄCHST WEITER</div>
  <p class="txt">Der internationale Handel mit illegalen Imitaten und Produktfälschungen verursacht laut einer neuen Studie der Europäische Beobachtungsstelle und der Organisation für wirtschaftliche Zusammenarbeit und Entwicklung (OWZE) einen finanziellen Schaden von bis zu 340 Milliarden Euro pro...</p>
</article>
<article class="post" style="left:424px;top:724px">
  <div class="date">6. Juni 2016</div>
  <div class="ttl" style="border:none">PRODUKTPIRATERIE: ZAHL DER FÄLSCHUNGEN WÄCHST WEITER</div>
  <p class="txt">Der internationale Handel mit illegalen Imitaten und Produktfälschungen verursacht laut einer neuen Studie der Europäische Beobachtungsstelle und der Organisation für wirtschaftliche Zusammenarbeit und Entwicklung (OWZE) einen finanziellen Schaden von bis zu 340 Milliarden Euro pro...</p>
</article>
<div class="btn" style="left:315px;top:818px;width:62px;height:15px">ZUM BLOG</div>

<!-- English blog -->
<h2 class="sec-head" style="top:845px">DIE LETZTEN ARTIKEL AUS UNSEREM ENGLISCHEN BLOG<div class="rule"></div></h2>
<article class="post" style="left:134px;top:871px">
  <div class="date">6. Juni 2016</div>
  <div class="ttl">VALMORA SHOES:<br>RED SOLE DECORATIVE, BUT NOT DISTINCTIVE</div>
  <p class="txt">In a decision of 27 April 2016, the Swiss Federal Adminstrative Court confirmed the IPO’s refusal to grant Valmora’s “red sole” application protection for high heels in Switzerland...</p>
</article>
<article class="post" style="left:279px;top:871px">
  <div class="date">6. Juni 2016</div>
  <div class="ttl">VALMORA SHOES:<br>RED SOLE DECORATIVE, BUT NOT DISTINCTIVE</div>
  <p class="txt">In a decision of 27 April 2016, the Swiss Federal Adminstrative Court confirmed the IPO’s refusal to grant Valmora’s “red sole” application protection for high heels in Switzerland...</p>
</article>
<article class="post" style="left:424px;top:871px">
  <div class="date">6. Juni 2016</div>
  <div class="ttl">VALMORA SHOES:<br>RED SOLE DECORATIVE, BUT NOT DISTINCTIVE</div>
  <p class="txt">In a decision of 27 April 2016, the Swiss Federal Adminstrative Court confirmed the IPO’s refusal to grant Valmora’s “red sole” application protection for high heels in Switzerland...</p>
</article>
<div class="btn" style="left:315px;top:956px;width:62px;height:15px">ZUM BLOG</div>

<!-- Awards -->
<h2 class="sec-head" style="top:989px">UNSERE AUSZEICHNUNGEN<div class="rule"></div></h2>
<div class="abs awards">
  <div><span role="img" aria-label="Auszeichnungs-Siegel" style="width:60px;height:60px;border-radius:50%;background:radial-gradient(circle,#f3e4b0,#b8923a)"></span></div>
  <div><span role="img" aria-label="Ranking-Auszeichnung" style="width:49px;height:72px;background:linear-gradient(160deg,#c9a227,#9c7a10)"></span></div>
  <div><span role="img" aria-label="Global-Awards-Auszeichnung" style="width:83px;height:46px;background:#111"></span></div>
  <div class="cta">Lorem ipsum dolor sit amet, consectetuer adipiscing elit. Aenean commodo ligula eget dolor. Aenean massa.
    <span class="btn" style="position:static;width:62px;height:14px;margin-top:12px">MEHR ERFAHREN</span></div>
</div>
<div class="abs pdots"><i style="background:var(--orange)"></i><i></i></div>

<!-- Footer -->
<footer class="abs footer">
  <span class="ficon" style="left:134px;top:9px"></span>
  <div class="fcol" style="left:145px">Lindenhofstr. 12-14<br>D-60311 Frankfurt am Main<br>Deutschland – Germany</div>
  <span class="ficon" style="left:279px;top:9px"></span>
  <span class="ficon" style="left:279px;top:20px"></span>
  <span class="ficon" style="left:279px;top:31px"></span>
  <div class="fcol" style="left:290px">Tel: +49 (0) 69 / 555 014 - 0<br>Fax: +49 (0) 69 / 555 014 - 199<br>info[at]juris-vantor.com</div>
  <ul class="fcol fl" style="left:424px"><li>Datenschutzerklarung</li><li>Impressum</li><li>Sitemap</li></ul>
</footer>

</body>
</html>
```